Gourmet Restaurant take out menu

We need a take out menu design that is trendy for a casual upscale Italian restaurant with a vast menu. This menu must be able to be 4 color and reproducible in large quantities to be bulked mailed or inserted into a daily paper. It must also maintain a theme that can be crossed over to our in house dining menu and specials menu.
OUR WEBSITE:
www.bellavistoplates.example
For the content, go to the Menu section of our website. We are interested in the design scheme and a template to use.
Target Market(s)
families, sinle individuals seeking take out meals and delivery
Industry/Entity Type
Restaurant
Look and feel
Each slider illustrates characteristics of the customer's brand and the style your logo design should communicate.

```html
<!DOCTYPE html>
<html lang="en">
<head>
<meta charset="utf-8">
<title>Bella Visto Plates – Take Out Menu</title>
<link rel="stylesheet" href="https://fonts.googleapis.com/css2?family=Rokkitt:wght@600;700&family=Crimson+Text:wght@400;600&display=swap">
<style>
:root{
  --red:#971c1e;
  --beige:#dccba7;
  --panel:#ece5d3;
  --ink:#22180f;
  --accent:#9a2a20;
}
*{margin:0;padding:0;box-sizing:border-box}
html,body{width:1200px;height:777px;overflow:hidden;background:var(--red)}
body{position:relative;font-family:"Crimson Text",Georgia,serif;color:var(--ink)}
.page{position:absolute;top:0;height:777px;overflow:hidden}
.page-left{left:0;width:605px;background:var(--beige);border-right:14px solid var(--red)}
.page-right{left:605px;width:595px;background:var(--red)}
.sheet{position:absolute;left:8px;top:112px;width:587px;height:665px;background:var(--beige);border-radius:22px 0 0 0}
.section-title{position:absolute;font-family:"Rokkitt",Georgia,serif;font-weight:700;color:var(--ink);text-align:center;font-size:19px;line-height:1}
.section-title.small{font-size:12px}
.tagline{position:absolute;border:1px solid var(--accent);border-top:none;color:var(--accent);font-size:5px;letter-spacing:.2px;text-align:center;text-transform:uppercase;display:flex;align-items:center;justify-content:center;line-height:1.4;padding:0 6px;white-space:nowrap}
.tagline.boxed{border-top:1px solid var(--accent)}
.tagline.two-line{white-space:normal}
.panel{position:absolute;background:var(--panel);padding:6px 8px;overflow:hidden}
.item{margin-bottom:2px}
.row{display:flex;justify-content:space-between;font-size:7.4px;line-height:1.15;font-weight:600}
.row span:last-child{font-weight:400;white-space:nowrap;padding-left:4px}
.desc{font-size:4.2px;line-height:1.3;color:#3a2e22;padding-right:34px}
.list .row{font-size:7.4px;line-height:1.1;margin-bottom:1.6px}
.list.compact .row{font-size:7px;line-height:8px;margin-bottom:1px}
.two-col{display:flex;gap:12px}
.two-col>div{flex:1}
.heart .item{margin-bottom:8px}
.photo{position:absolute}
.logo-name{font-family:"Rokkitt",Georgia,serif;font-weight:600;color:var(--red);text-align:center}
.contact h3{font-family:"Rokkitt",Georgia,serif;font-weight:700;color:var(--red);font-size:15px;margin-bottom:5px}
.contact p{color:var(--red);font-size:10px;line-height:1.6}
.toppings{position:absolute;left:618px;top:162px;width:286px;color:var(--accent);font-size:4.4px;line-height:1.9;text-align:center;text-transform:uppercase}
.toppings .lead{font-size:6px;text-transform:none}
.toppings .plain{text-transform:none}
</style>
</head>
<body>

<section class="page page-left">
  <h2 class="section-title" style="left:16px;top:16px;width:280px">Fish and Seafood</h2>
  <div class="tagline" style="left:28px;top:38px;width:254px;height:14px">Served with a house salad and bread</div>
  <div class="panel" style="left:16px;top:53px;width:280px;height:233px">
    <div class="item"><p class="row"><span>Fried Shrimp Platter</span><span>16.99</span></p><p class="desc">Complemented with French fries, coleslaw and our homemade cocktail sauce.</p></div>
    <div class="item"><p class="row"><span>Gourmet Seafood</span><span>24.99</span></p><p class="desc">Gulf shrimp, jumbo sea scallops, littleneck clams, sweet mussels in a spicy marinara sauce with garlic, fresh herbs over linguini.</p></div>
    <div class="item"><p class="row"><span>Horseradish Encrusted Salmon</span><span>17.99</span></p><p class="desc">Accompanied with a whole grain mustard sauce, savory rice, seasonal vegetable.</p></div>
    <div class="item"><p class="row"><span>Scallops Piccata</span><span>20.99</span></p><p class="desc">Capers and spinach in a fresh lemon butter sauce, served over angel hair pasta.</p></div>
    <div class="item"><p class="row"><span>Flounder Puttanesca</span><span>17.99</span></p><p class="desc">Sautéed flounder filet topped with our homemade puttanesca sauce, served with rice.</p></div>
    <div class="item"><p class="row"><span>Fried Flounder</span><span>17.99</span></p><p class="desc">Panko breadcrumb encrusted flounder, served with coleslaw and cajun French fries.</p></div>
    <div class="item"><p class="row"><span>Brewhouse Fish and Chips</span><span>13.99</span></p><p class="desc">Beer battered, served with seasoned French fries and tartar sauce.</p></div>
    <div class="item"><p class="row"><span>Shrimp Scampi</span><span>18.99</span></p><p class="desc">Plum tomatoes, lemon butter sauce, seasoned with fresh basil and garlic over linguini.</p></div>
    <div class="item"><p class="row"><span>Shrimp Parmigiana</span><span>17.99</span></p><p class="desc">Topped with our homemade tomato sauce, mozzarella cheese, served with a side of linguini.</p></div>
    <div class="item"><p class="row"><span>Tilapia Gracina</span><span>18.99</span></p><p class="desc">Coated in a parmesan egg batter topped with lump crab meat, finished with a tomato basil butter sauce, served over spinach.</p></div>
    <div class="item"><p class="row"><span>Sesame Seared Tuna</span><span>21.99</span></p><p class="desc">Black and white sesame seed encrusted ahi tuna, served with vegetables in a sweet hoisin sauce and wasabi mashed.</p></div>
    <div class="item"><p class="row"><span>Stuffed Flounder</span><span>20.99</span></p><p class="desc">Stuffed with jumbo lump crab, drizzled with a lemon butter sauce, served with mashed potatoes and mixed vegetables.</p></div>
    <div class="item"><p class="row"><span>Salmon Chardonnay</span><span>17.99</span></p><p class="desc">Oven braised salmon in an unoaked Chardonnay sauce, served with mashed potatoes and mixed vegetables.</p></div>
  </div>

  <h2 class="section-title" style="left:16px;top:298px;width:280px">Childrens Menu</h2>
  <div class="panel list" style="left:16px;top:320px;width:280px;height:104px;padding-top:9px">
    <p class="row"><span>Cheeseburger and Fries</span><span>5.99</span></p>
    <p class="row"><span>Chicken Fingers and Fries</span><span>6.59</span></p>
    <p class="row"><span>Grilled Cheese and Fries</span><span>5.99</span></p>
    <p class="row"><span>Grilled Chicken Breast with Buttered Pasta</span><span>6.99</span></p>
    <p class="row"><span>Linguini and Meatball</span><span>6.99</span></p>
    <p class="row"><span>Mac and Cheese</span><span>4.99</span></p>
    <p class="row"><span>Mini Pizza</span><span>5.99</span></p>
    <p class="row"><span>Ravioli and Meatball</span><span>6.99</span></p>
    <p class="row"><span>Sliders (2) and Fries</span><span>5.99</span></p>
  </div>

  <h2 class="section-title" style="left:16px;top:434px;width:280px">Beverages</h2>
  <div class="panel list" style="left:16px;top:456px;width:280px;height:88px;padding-top:10px">
    <p class="row"><span>16 oz Bottled Tea</span><span>1.99</span></p>
    <p class="row"><span>Home-Brewed Iced Tea</span><span>1.99</span></p>
    <p class="row"><span>20 oz Bottles</span><span>1.99</span></p>
    <p class="row"><span>(Cola, Diet Cola, Orange, Ginger Ale, Lemon-Lime, Root Beer)</span><span></span></p>
    <p class="row"><span>2 Liter Bottles</span><span>2.99</span></p>
    <p class="row"><span>(Cola, Diet Cola, Orange, Ginger Ale, Lemon-Lime, Root Beer)</span><span></span></p>
    <p class="row"><span>16 oz Bottled Water</span><span>1.59</span></p>
  </div>

  <h2 class="section-title" style="left:306px;top:16px;width:278px">Heart Healthy</h2>
  <div class="tagline" style="left:318px;top:38px;width:254px;height:14px">Served with a house salad and bread</div>
  <div class="panel heart" style="left:306px;top:53px;width:278px;height:491px;padding-top:8px">
    <div class="item"><p class="row"><span>Broiled Scallops</span><span>13.99</span></p><p class="desc">Sweet lime sauce, complemented with rice, chef's vegetable. Nutritional Value: Calories 265; Protein 22.7g; Carbs 31.3g; Total Fat 4g; Sat Fat 1g; Cholesterol 37mg; Sodium 463mg; Potassium 404mg</p></div>
    <div class="item"><p class="row"><span>Eggplant Pomodoro</span><span>10.99</span></p><p class="desc">Pasta diced eggplant, plum tomatoes, green olives and capers sautéed in olive oil and garlic, served over angel hair. Nutritional Value: Calories 252; Protein 27g; Carbs 15g; Total Fat 5g; Sat Fat 1g; Cholesterol 66mg; Potassium 444mg; Sodium 517mg</p></div>
    <div class="item"><p class="row"><span>Chicken and Asparagus</span><span>11.99</span></p><p class="desc">Plum tomatoes, asparagus, garlic and feta cheese, served over penne pasta, finished with fresh herbs, parmesan cheese. Nutritional Value: Calories 282; Protein 19g; Carbs 49g; Total Fat 7g; Sat Fat 3g; Cholesterol 21mg; Potassium 416mg; Sodium 467mg</p></div>
    <div class="item"><p class="row"><span>Gnocchi Pancetta</span><span>9.99</span></p><p class="desc">Pancetta, plum tomatoes, oil, garlic with parmesan cheese. Nutritional Value: Calories 377; Protein 14g; Carbs 63g; Total Fat 7g; Sat Fat 3g; Cholesterol 16mg; Potassium 329mg; Sodium 686mg</p></div>
    <div class="item"><p class="row"><span>Flounder Olivio</span><span>12.99</span></p><p class="desc">Extra virgin olive oil, garlic, onion, capers, green olives, julienne jalapeños, tomatoes, served with chef's vegetables. Nutritional Value: Calories 271; Protein 34g; Carbs 16g; Total Fat 8g; Sat Fat 1g; Cholesterol 52mg; Sodium 566mg</p></div>
    <div class="item"><p class="row"><span>Lemon Garlic Tilapia</span><span>12.99</span></p><p class="desc">Tilapia sautéed with lemon, garlic, parsley, pepper and a touch of butter, served with chef's vegetable. Nutritional Value: Calories 271; Protein 26g; Carbs 19g; Total Fat 9g; Sat Fat 2g; Cholesterol 58mg; Sodium 274</p></div>
    <div class="item"><p class="row"><span>Herb Filet</span><span>15.99</span></p><p class="desc">Filet of beef rubbed with an herb butter and grilled, accompanied with vegetables. Nutritional Value: Calories 338; Protein 39g; Carbs 18g; Total Fat 14g; Sat Fat 5g; Cholesterol 80mg; Potassium 462mg; Sodium 442mg</p></div>
    <div class="item"><p class="row"><span>Lemon Caper Salmon</span><span>12.99</span></p><p class="desc">Poached in a creamy lemon caper sauce, served with rice pilaf, steamed chef's choice vegetables. Nutritional Value: Calories 370; Protein 26.8g; Carbs 11.3g; Total Fat 16g; Sat Fat 4g; Cholesterol 73mg; Potassium 500mg; Sodium 586mg</p></div>
    <div class="item"><p class="row"><span>Penne Siciliano</span><span>10.99</span></p><p class="desc">Cherry tomatoes, asparagus, goat cheese, finished with fresh basil, garlic, extra virgin olive oil. Nutritional Value: Calories 381; Protein 15g; Carbs 60g; Total Fat 9g; Sat Fat 4g; Cholesterol 25mg; Potassium 427mg; Sodium 329mg</p></div>
    <div class="item"><p class="row"><span>Tuna Tempero</span><span>13.99</span></p><p class="desc">Ahi tuna, olive relish, served with rice, broccoli crowns. Nutritional Value: Calories 184; Protein 34g; Carbs 1g; Total Fat 5g; Sat Fat 1g; Cholesterol 61mg; Potassium 636 mg; Sodium 266mg</p></div>
    <div class="item"><p class="row"><span>Grilled Miso Salmon</span><span>12.99</span></p><p class="desc">Glazed with an infused soy sauce and sweet rice wine reduction, finished with fresh cilantro, sesame seeds, served with steamed Asian vegetables. Nutritional Value: Calories 282; Protein 29g; Carbs 4g; Total Fat 10g; Sat Fat 2g; Cholesterol 78mg; Sodium 382mg</p></div>
  </div>

  <div style="position:absolute;left:16px;top:547px;width:568px;height:3px;background:var(--red)"></div>

  <div class="logo-name" style="position:absolute;left:60px;top:568px;width:200px">
    <div style="font-size:30px;line-height:1">Bella Visto</div>
    <div style="font-size:11px;letter-spacing:3px;margin-top:3px">PLATES</div>
  </div>
  <div class="contact" style="position:absolute;left:306px;top:562px">
    <h3>Our Location</h3>
    <p>518 Orchard Lane<br>Maple Ridge, NJ</p>
  </div>
  <div class="contact" style="position:absolute;left:428px;top:560px">
    <h3>Contact</h3>
    <p>(555) 210-4400<br>(555) 210-4411<br>hello@bellavistoplates.example</p>
  </div>

  <div class="photo" role="img" aria-label="Photo of the restaurant dining room and bar" style="left:0;top:640px;width:591px;height:137px;background:linear-gradient(180deg,#5a3a24 0%,#8a5a34 40%,#3e2618 100%)"></div>
</section>

<section class="page page-right">
  <div class="photo" role="img" aria-label="Photo of a pizza slice" style="left:0;top:0;width:200px;height:118px;background:radial-gradient(ellipse at 50% 40%,#d99a3a 0%,#b2401e 55%,#5a1a10 100%)"></div>
  <div class="photo" role="img" aria-label="Photo of a cheeseburger" style="left:379px;top:0;width:216px;height:118px;background:radial-gradient(ellipse at 50% 50%,#e0a640 0%,#7a3a1c 60%,#3a1a0e 100%)"></div>
  <div class="sheet"></div>
  <svg style="position:absolute;left:180px;top:0" width="240" height="140" viewBox="0 0 240 140" aria-hidden="true">
    <path d="M0 140 C10 40 90 8 150 8 C200 8 235 30 240 50 L240 140 Z" fill="#971c1e"/>
    <path d="M10 140 C20 52 95 18 150 18 C198 18 232 40 240 60 L240 140 Z" fill="#dccba7"/>
  </svg>
  <div class="logo-name" style="position:absolute;left:220px;top:62px;width:200px">
    <div style="font-size:26px;line-height:1">Bella Visto</div>
    <div style="font-size:10px;letter-spacing:3px;margin-top:2px">PLATES</div>
  </div>
</section>

<h2 class="section-title" style="left:618px;top:136px;width:286px;font-size:20px">Gourmet Pizza</h2>
<div class="toppings">
  <p class="lead">Toppings for 1.99</p>
  <p>Ham • Broccoli • Extra Cheese • Tomatoes hot or sweet peppers • Roasted peppers • Pepperoni • Spinach • Italian sausage • Black olives • Green peppers • Mushrooms • Onions • Anchovies • Grilled chicken</p>
  <p>Meatball bacon and ricotta 3.00</p>
  <p class="plain">10" Individual, 12" Medium, 16" Large</p>
  <p class="plain">Pizza By The Slice - Plain 1.99, Veggie 2.99</p>
</div>
<div class="panel" style="left:618px;top:222px;width:286px;height:236px">
  <div class="item"><p class="row"><span>Plain Cheese</span><span>8.99/11.99/12.99</span></p></div>
  <div class="item"><p class="row"><span>Traditional White</span><span>8.59/11.59/13.99</span></p><p class="desc">Olive oil, garlic, mozzarella cheese.</p></div>
  <div class="item"><p class="row"><span>Chicken Bacon Ranch</span><span>10.99/14.99/16.99</span></p><p class="desc">Garlic chicken, bacon, pepperjack and cheddar cheese, red onions, diced tomatoes, drizzle of ranch dressing.</p></div>
  <div class="item"><p class="row"><span>Bronx Bomber</span><span>11.99/14.99/16.99</span></p><p class="desc">Sausage, prosciutto ham, oregano, crumbled bleu and mozzarella cheese.</p></div>
  <div class="item"><p class="row"><span>Buffalo Chicken</span><span>10.99/14.99/16.99</span></p><p class="desc">Buffalo sauce, chicken, mozzarella cheese, side of bleu cheese dressing.</p></div>
  <div class="item"><p class="row"><span>Gourmet Special</span><span>12.99/16.99/18.99</span></p><p class="desc">Pepperoni, sausage, bell peppers, mushrooms, onion, mozzarella cheese.</p></div>
  <div class="item"><p class="row"><span>Margarita</span><span>8.99/11.99/13.99</span></p><p class="desc">Fresh basil, tomato, buffalo mozzarella cheese.</p></div>
  <div class="item"><p class="row"><span>Roasted Vegetable</span><span>11.99/14.99/16.99</span></p><p class="desc">Eggplant, red and yellow peppers, onions, artichokes, Kalamata olives, tomatoes, mozzarella cheese. Veggie Lover Olive oil, garlic, broccoli, spinach, tomato, mozzarella cheese.</p></div>
  <div class="item"><p class="row"><span>Sweet Hawaiian</span><span>11.99/14.99/16.99</span></p><p class="desc">Pineapple, tomatoes, ham, mozzarella cheese.</p></div>
  <div class="item"><p class="row"><span>Spinach and Artichoke</span><span>8.99/11.99/12.99</span></p><p class="desc">Spinach, artichoke hearts, buffalo mozzarella, parmesan cheese.</p></div>
  <div class="item"><p class="row"><span>Philly Cheese Steak</span><span>11.99/14.99/16.99</span></p><p class="desc">Philly steak, green peppers, onions, provolone, American cheese.</p></div>
  <div class="item"><p class="row"><span>Grandma's Pie</span><span>14.99</span></p><p class="desc">Thin crust pizza topped with mozzarella, tomato sauce, buffalo mozzarella, fresh basil, olive oil. (One Size)</p></div>
</div>

<h2 class="section-title small" style="left:618px;top:465px;width:286px">Hot Subs - Add Cheese for $0.59</h2>
<div class="panel list compact two-col" style="left:618px;top:480px;width:286px;height:104px;padding-top:7px">
  <div>
    <p class="row"><span>Cheesesteak</span><span>6.59</span></p>
    <p class="row"><span>Bacon Cheesesteak</span><span>7.59</span></p>
    <p class="row"><span>Steak Sub</span><span>6.29</span></p>
    <p class="row"><span>Chicken Parmigiana</span><span>6.99</span></p>
    <p class="row"><span>Pepper, Egg, &amp; Cheese</span><span>6.29</span></p>
    <p class="row"><span>Pizza Cheesesteak</span><span>6.99</span></p>
    <p class="row"><span>Meatball Parmigiana</span><span>6.99</span></p>
    <p class="row"><span>Mushroom Cheesesteak</span><span>6.99</span></p>
    <p class="row"><span>Veal Parmigiana</span><span>7.99</span></p>
  </div>
  <div>
    <p class="row"><span>Pepper Cheesesteak</span><span>6.99</span></p>
    <p class="row"><span>Vegetarian with Cheese</span><span>6.59</span></p>
    <p class="row"><span>Eggplant Parmigiana</span><span>6.59</span></p>
    <p class="row"><span>Chicken Cheesesteak</span><span>6.99</span></p>
    <p class="row"><span>Sausage Parmigiana</span><span>7.59</span></p>
    <p class="row"><span>Grilled Chicken</span><span>6.59</span></p>
    <p class="row"><span>Cheeseburger Sub</span><span>7.59</span></p>
    <p class="row"><span>Chicken Cacciatore</span><span>7.59</span></p>
    <p class="row"><span>Steak Cacciatore</span><span>7.59</span></p>
    <p class="row"><span>Sausage, Peppers, &amp; Onion</span><span>6.99</span></p>
  </div>
</div>

<h2 class="section-title small" style="left:618px;top:594px;width:286px">Cold Subs - Add Cheese for $0.59</h2>
<div class="panel list compact two-col" style="left:618px;top:609px;width:286px;height:56px;padding-top:8px">
  <div>
    <p class="row"><span>Regular Italian</span><span>6.59</span></p>
    <p class="row"><span>Tuna</span><span>6.59</span></p>
    <p class="row"><span>Roast Beef</span><span>7.59</span></p>
    <p class="row"><span>Imported Ham</span><span>6.59</span></p>
  </div>
  <div>
    <p class="row"><span>Roast Turkey</span><span>6.99</span></p>
    <p class="row"><span>Provolone</span><span>6.59</span></p>
    <p class="row"><span>Capicola, Salami, &amp; Provolone</span><span>6.99</span></p>
    <p class="row"><span>Chicken Salad</span><span>6.99</span></p>
  </div>
</div>

<h2 class="section-title" style="left:618px;top:674px;width:286px">Sandwiches</h2>
<div class="tagline boxed" style="left:628px;top:695px;width:266px;height:14px;font-size:4.2px;letter-spacing:0">8oz certified black angus beef, served on a kaiser roll with French fries and a fried pickle</div>
<div class="panel" style="left:618px;top:716px;width:286px;height:61px;padding-top:9px">
  <div class="item"><p class="row"><span>Bruschetta Chicken</span><span>7.59</span></p><p class="desc">Bruschetta salsa, pesto, provolone cheese, balsamic drizzle on a French baguette, served with French fries.</p></div>
  <div class="item"><p class="row"><span>Chicken Parmigiana</span><span>7.59</span></p><p class="desc">Served on a Kaiser roll with French fries.</p></div>
</div>

<div class="panel" style="left:912px;top:128px;width:282px;height:244px">
  <div class="item"><p class="row"><span>Chicken Portabella</span><span>8.59</span></p><p class="desc">Grilled chicken, roasted red peppers, grilled portabella, lettuce, provolone and a creamy peppercorn aioli, on a French baguette, served with French fries.</p></div>
  <div class="item"><p class="row"><span>Classic BLT</span><span>6.59</span></p><p class="desc">Served with potato chips.</p></div>
  <div class="item"><p class="row"><span>Crab Cake</span><span>9.99</span></p><p class="desc">Lettuce, tomato and tartar sauce, served on a Kaiser roll with French fries.</p></div>
  <div class="item"><p class="row"><span>Fish Taco</span><span>7.99</span></p><p class="desc">Fried wahoo in a flour tortilla with chipotle mayo, shredded lettuce, red onion and pico de gallo, finished with an avocado cream, served with potato chips.</p></div>
  <div class="item"><p class="row"><span>French Dip</span><span>8.59</span></p><p class="desc">Thinly sliced roast beef on a French baguette served with au jus, creamy horseradish sauce and French fries.</p></div>
  <div class="item"><p class="row"><span>Grilled Cheese</span><span>2.99</span></p><p class="desc">Served with potato chips. Add bacon, ham or tomato. 4.99</p></div>
  <div class="item"><p class="row"><span>Grilled Chicken</span><span>6.99</span></p><p class="desc">Lettuce, tomato, served on a Kaiser roll with French fries.</p></div>
  <div class="item"><p class="row"><span>Grilled Chicken Club</span><span>8.99</span></p><p class="desc">Bacon, avocado, Swiss cheese, lettuce, tomato and roasted garlic mayonnaise on a French baguette.</p></div>
  <div class="item"><p class="row"><span>Italian Eggplant</span><span>7.99</span></p><p class="desc">Grilled eggplant, roasted red peppers, red onion, melted mozzarella and garlic aioli on a French baguette.</p></div>
  <div class="item"><p class="row"><span>Roasted Turkey Cobb</span><span>8.99</span></p><p class="desc">Roasted turkey breast, lettuce, tomatoes, avocado, bacon, bleu cheese dressing and Dijon mayonnaise, served on a French baguette.</p></div>
  <div class="item"><p class="row"><span>Tuna Melt</span><span>6.99</span></p><p class="desc">Served with French fries.</p></div>
  <div class="item"><p class="row"><span>Turkey Club</span><span>7.59</span></p><p class="desc">Served with potato chips.</p></div>
</div>

<h2 class="section-title" style="left:912px;top:386px;width:282px">Awesome Burgers</h2>
<div class="tagline boxed two-line" style="left:926px;top:411px;width:254px;height:21px">8oz certified black angus beef, served on a kaiser roll<br>with French fries and a fried pickle</div>
<div class="panel" style="left:912px;top:436px;width:282px;height:156px">
  <div class="item"><p class="row"><span>Cheeseburger</span><span>7.99</span></p></div>
  <div class="item"><p class="row"><span>Bacon Cheddar</span><span>8.99</span></p><p class="desc">Applewood smoked bacon, sharp cheddar.</p></div>
  <div class="item"><p class="row"><span>Blue Cheese BLT</span><span>9.59</span></p><p class="desc">Bacon, lettuce, tomato, onion, mayonnaise, bleu cheese.</p></div>
  <div class="item"><p class="row"><span>California</span><span>9.99</span></p><p class="desc">Avocado, roasted green chilies, pepper jack cheese, chipotle mayo, ranch dressing.</p></div>
  <div class="item"><p class="row"><span>Gourmet Sliders</span><span>8.99</span></p><p class="desc">3 bite-sized burgers with American cheese on mini potato rolls.</p></div>
  <div class="item"><p class="row"><span>Mushroom Swiss</span><span>8.59</span></p><p class="desc">Sautéed mushrooms, onions and mayo topped with Swiss cheese.</p></div>
  <div class="item"><p class="row"><span>Portabella</span><span>8.59</span></p><p class="desc">Angus burger, roasted portabella, melted provolone cheese.</p></div>
  <div class="item"><p class="row"><span>Pub</span><span>9.99</span></p><p class="desc">Steak sauce and mayo, topped with onion rings, bleu cheese.</p></div>
  <div class="item"><p class="row"><span>Smokehouse Barbecue</span><span>9.99</span></p><p class="desc">Smoked bacon, melted cheddar cheese, crispy onion strings, tangy barbecue-ranch sauce.</p></div>
</div>

<h2 class="section-title" style="left:912px;top:604px;width:282px">Gorbolis &amp; Gorzones</h2>
<div class="tagline boxed" style="left:920px;top:624px;width:266px;height:12px;font-size:4px;letter-spacing:0">Available in spinach, sundried tomato and flour tortilla, served with French fries &amp; a fried pickle</div>
<div class="panel" style="left:912px;top:640px;width:282px;height:137px;padding-top:5px">
  <div class="item"><p class="row"><span>Buffalo Chicken</span><span>7.99</span></p><p class="desc">Buffalo sauce, shredded lettuce, bleu cheese dressing.</p></div>
  <div class="item"><p class="row"><span>Caprese Wrap</span><span>8.99</span></p><p class="desc">Chicken, buffalo mozzarella, tomato, Romaine lettuce drizzled with a balsamic reduction.</p></div>
  <div class="item"><p class="row"><span>Chicken Caesar</span><span>7.99</span></p><p class="desc">Romaine lettuce, classic Caesar salad dressing.</p></div>
  <div class="item"><p class="row"><span>Italian Chicken</span><span>7.99</span></p><p class="desc">Breaded chicken tenders, cheddar cheese, lettuce, tomato, ranch dressing.</p></div>
  <div class="item"><p class="row"><span>Roman</span><span>7.99</span></p><p class="desc">Chicken, roasted peppers, shredded lettuce, basil mayonnaise, mozzarella cheese.</p></div>
  <div class="item"><p class="row"><span>Santa Fe</span><span>8.59</span></p><p class="desc">Chicken, guacamole, tomato, cheddar cheese, lettuce, tortilla strips, served with a side of salsa.</p></div>
  <div class="item"><p class="row"><span>The Philly</span><span>7.99</span></p><p class="desc">Philly steak, provolone, sautéed onions, peppers.</p></div>
</div>

</body>
</html>
```